Packaging and labelling for Swiss made Organic CBD Oil

Visit our website www.velmarotiva.com
We have not put any product on yet as require packaging and label design .
Website will give you a great feel for the company and how we have used
the logo . The Drevask cbd product shown is a company similar to ourselves with similar core values , we liked the clean packaging design they have .

Im happy if you want use the mandala symbol in our logo separate from
VELMARO, to separate and use the mandala symbol as a larger icon than
it appears in our logo
Clean , Pure , organic feel. Like the product to look pharmaceutical and life changing not gimmicky.
Colours to go with or be the same as our logo colours
But not too cold and clinical
Bottle size 84mm x 25mm
Label size 75mm x 30mm
Box 30mm x 30mm x 100mm
6 products
Full Spectrum :
500mg CBD (5%)
1000mg CBD ( 10% )
1500mg CBD (15%)
2000mg CBD ( 20% )
Broad spectrum THC Free
500mg CBD (5%)
Pets
500mg Broad Spectrum THC Free
Updates

Would like the design to be more modern than traditional

LABEL Information Front of Bottle - Logo VELMARO & Mandala - Mandala can be used separately as design symbol Organic Cannabis Oil 1500mg CBD (15%) Ful Spectrum 10ml Back of bottle Ingredients: Organic Cannabis Oil Extract Organic Sunflower Seed Oil THC - 0.2% Certified Swiss Organic Cultivation Shake well before use. Store in a cool , dry place and out of the each of children BOX information Front and rear Logo - VELMARO & Mandala - Mandala can be used separately as a design symbol Organic Cannabis Oil 1500mg CBD (15%) Full Spectrum Sides x 2 This product is a food supplement and is not intended to diagnose, treat, cure or prevent any disease If you are pregnant, lactating or taking any medication consult your health care practitioner Suitable for vegetarians and vegans Ingredients Organic Cannabis Oil extract Organis Sunflower Oil Store in a cool ,dry place, out of the reach of children Recommended Use 1-5 drops ( 1 drop = 7.5mg CBD ) Subject to body weight and personal requirement - visit www.velmarotiva for more information 100% Natural 100% Organic GMO free 100% Vegan ( symbol with each ) Expiry date see bottle label Cultivated and manufactured in Switzerland

Target Market(s)

age 40 - 80

Font styles to use
Other font styles liked:
• In our website we have used Open Sans for the copy and Lato for headings .

Requirements
Must have
• look like an Industry leader
Velmaro will change the quality of peoples lives and in some cases may
even save lives so want look powerful and credible
Our Mission is - Through Delivering Pure , Premium , Organic products we will educate, inform and help people achieve healthier , happier lifestyles
Nice to have
• Colours to look good with our logo colours or be the same as our logo
colours
Logo Font - Avenir Black and Avenir Book

Font used in website - Content - Open Sans / Headings - Lato
If you have another font for the packaging information that will go well with
our logo, I'm happy for you to use your skills

```html
<!DOCTYPE html>
<html lang="en">
<head>
<meta charset="utf-8">
<title>Velmaro – Organic Cannabis Oil Packaging</title>
<link rel="stylesheet" href="https://fonts.googleapis.com/css2?family=Nunito+Sans:wght@300;400;800&display=swap">
<style>
  :root {
    --page-bg: #f4f4f6;
    --panel-white: #ffffff;
    --panel-shade: #f0f0f1;
    --mint: #a2d9d6;
    --mint-text: #8ccdc9;
    --ink: #2a2a2a;
    --on-mint: #ffffff;
  }
  * { box-sizing: border-box; margin: 0; padding: 0; }
  html, body {
    width: 1200px;
    height: 1065px;
    overflow: hidden;
    background: var(--page-bg);
    font-family: "Nunito Sans", "Avenir", sans-serif;
  }
  .canvas { position: relative; width: 1200px; height: 1065px; }

  .panel {
    position: absolute;
    display: flex;
    flex-direction: column;
    background: var(--panel-white);
    box-shadow: 0 2px 10px rgba(0,0,0,0.06);
  }
  .panel__top {
    position: relative;
    background: linear-gradient(90deg, var(--panel-shade) 0%, var(--panel-white) 45%, var(--panel-shade) 100%);
  }
  .panel__band {
    position: relative;
    flex: 1;
    background: var(--mint);
    color: var(--on-mint);
    font-weight: 300;
  }

  .wordmark {
    position: absolute;
    left: 0; right: 0;
    text-align: center;
    font-weight: 800;
    color: var(--ink);
    letter-spacing: 0.04em;
  }
  .tagline {
    position: absolute;
    left: 0; right: 0;
    text-align: center;
    font-weight: 300;
    color: var(--mint-text);
  }
  .strength, .spec {
    position: absolute;
    line-height: 1.3;
  }

  /* Bottle label */
  .label { width: 208px; height: 436px; top: 444px; }
  .label--left { left: 221px; }
  .label--right { left: 829px; top: 442px; }
  .label .panel__top { height: 262px; }
  .label .wordmark { top: 124px; font-size: 27px; }
  .label .tagline { top: 186px; font-size: 15px; }
  .label .strength { left: 12px; top: 22px; font-size: 14px; }
  .label .spec { left: 18px; top: 98px; font-size: 13px; line-height: 1.4; }

  /* Box front */
  .box { left: 501px; top: 88px; width: 275px; height: 873px; }
  .box .panel__top { height: 542px; }
  .box .wordmark { top: 320px; font-size: 42px; }
  .box .tagline { top: 470px; font-size: 20px; }
  .box .strength { left: 24px; top: 34px; font-size: 23px; }
  .box .spec { left: 20px; top: 204px; font-size: 21px; line-height: 1.38; }
</style>
</head>
<body>
<main class="canvas">

  <section class="panel label label--left" aria-label="Bottle label">
    <div class="panel__top">
      <p class="wordmark">VELMARO</p>
      <p class="tagline">Organic Cannabis Oil</p>
    </div>
    <div class="panel__band">
      <p class="strength">1000mg CBD<br>( 10% )</p>
      <p class="spec">500mg<br>Broad Spectrum<br>THC Free</p>
    </div>
  </section>

  <section class="panel box" aria-label="Box front">
    <div class="panel__top">
      <p class="wordmark">VELMARO</p>
      <p class="tagline">Organic Cannabis Oil</p>
    </div>
    <div class="panel__band">
      <p class="strength">1000mg CBD<br>( 10% )</p>
      <p class="spec">500mg<br>Broad Spectrum<br>THC Free</p>
    </div>
  </section>

  <section class="panel label label--right" aria-label="Bottle label">
    <div class="panel__top">
      <p class="wordmark">VELMARO</p>
      <p class="tagline">Organic Cannabis Oil</p>
    </div>
    <div class="panel__band">
      <p class="strength">1000mg CBD<br>( 10% )</p>
      <p class="spec">500mg<br>Broad Spectrum<br>THC Free</p>
    </div>
  </section>

</main>
</body>
</html>
```